Personal Branding - Pilot, Blogger, Speaker

I need a unique card that is remarkable and fits around me and my personal brand. I am an airline captain, blogger, and speaker. I want the card to have some element that is so unique the recipient will have to show someone else how bizarre and unique it is. I also want to stay within the bounds of professionalism. My card will be given out to other airlines to get a better flying job as well as people I want to come to my blog and hire me to speak at their event. I speak on motivation, life goals, learning, and time management. My brand is to inspire others to conquer fear and live remarkably. I want to include the color orange in my design.
Updates

My website is www.corwinteller.com to get an idea of who I am am what my brand is. I am a motivational speaker, blogger, and entrepreneur. My day job is a captain at an airline. I want to include the following info on my business card. I saw a card that had a crazy mouth on the back and when you hold it in front of your mouth it looks like you're making a silly face. Just one catchy idea I saw and liked. I really want something worth making a remark about when I walk away.Thank You for your designs. Orange, Black, Gray, Red, Corwin T. Teller Captain Valtrix 320 Skyloom Airlines 555.283.6094 corwinteller.com corwinteller@mailvale.net Speaker, Blogger, Entrepreneur

Reason: Extension to allow all designers time to complete their projects. Thank you for your designs. Incredible talent.

I've increased the budget of this project because I've shifted my focus slightly. I am including some links here to design ideas that I want to work towards. On the left side of a light gray card I want "corwinteller.com" in this font. I'm not sure if all black or black and red mix of letters will look best. Maybe the .com will be red https://cdn4.zq-img.net/entries/812/604337/2281-907-5521093877ab1c3d04e77f19/QX2_thumb.jpg This website will be the primary focus of the card. To drive traffic to my platform. (the original photo from https://www.tasklantern.net/contest/Logo-Design-for-blue-kite-NET-812.html) From the same photo I want the orange streak to come out of the bottom of the "b" in my name and arc back up and through the "o" in .com I want the rocket to be above the website name and flying upwards and to the right of the card. I like the angle of the rocket in the photo, it just needs to be flying the other direction so it passes through the letter "o" I like the colors of gray background, red rocket, orange streak. My contact info in black font will be below this logo and on the lower right of the card: Corwin T. Teller Captain, VTX-320, Skyloom Airlines 555.283.6094 corwinteller@mailvale.net On the back of the card is just this quote in black on a white background and the words "LIVE YOUR LEGEND" The quote will be in black letters and the "LIVE YOUR LEGEND" will be in red letters. β€œIt’s what you have always wanted to accomplish. Everyone, when they are young, knows what their Personal Legend is. At that point in their lives, everything is clear and everything is possible. They are not afraid to dream, and to yearn for everything they would like to see happen to them in their lives. But, as time passes, a mysterious force begins to convince them that it will be impossible for them to realize their Personal Legend.” ― Marten Vosk, The Lamplighter LIVE YOUR LEGEND. I'll try to submit a sketch somewhere on here. Thank You!!!

```html
<!DOCTYPE html>
<html lang="en">
<head>
<meta charset="utf-8">
<title>Corwin T. Teller – Business Card</title>
<link rel="stylesheet" href="https://fonts.googleapis.com/css2?family=Cinzel:wght@500&family=Questrial&display=swap">
<style>
  :root {
    --page: #e9e7e4;
    --card-white: #fbfbfb;
    --card-shade: #dedede;
    --orange: #dd8a2c;
    --ink: #2b2b2b;
    --gray-light: #8e8e8e;
    --gray-dark: #555555;
    --photo-sky: #6f9aa6;
    --photo-field: #8f9a5a;
    --photo-red: #a32a24;
  }
  * { margin: 0; padding: 0; box-sizing: border-box; }
  html, body { width: 1200px; height: 900px; overflow: hidden; background: var(--page); }
  .canvas {
    position: relative; width: 1200px; height: 900px;
    display: flex; align-items: center; justify-content: center; gap: 40px;
  }
  .card {
    position: relative; width: 540px; height: 310px; overflow: hidden;
    box-shadow: 0 6px 18px rgba(0,0,0,.18);
  }

  /* Front */
  .card-front {
    background: radial-gradient(circle at 55% 35%, var(--card-white) 0%, #f1f1f1 45%, var(--card-shade) 100%);
    font-family: "Questrial", sans-serif; color: var(--ink);
  }
  .photo {
    position: absolute; left: 22px; top: 18px; width: 258px; height: 168px;
    background: linear-gradient(180deg, var(--photo-sky) 0%, #a9c0c2 30%, #4e5b3c 40%, var(--photo-field) 55%, #7e8a4c 78%, var(--photo-red) 100%);
  }
  .identity { position: absolute; left: 282px; top: 128px; }
  .identity-name {
    font-family: "Cinzel", serif; font-weight: 500; font-size: 23px;
    color: var(--orange); letter-spacing: .5px; line-height: 1;
  }
  .identity-role { font-size: 12.5px; font-style: italic; color: var(--gray-dark); margin-top: 2px; }
  .contact-list { position: absolute; left: 22px; top: 198px; list-style: none; }
  .contact-item { display: flex; align-items: center; gap: 7px; font-size: 13px; height: 20px; }
  .contact-icon { width: 15px; height: 15px; flex: none; }
  .accent-tab {
    position: absolute; right: 0; top: 188px; width: 26px; height: 104px;
    background: var(--orange); border-radius: 5px 0 0 5px;
  }

  /* Back */
  .card-back {
    background: radial-gradient(ellipse at 50% 45%, var(--gray-light) 0%, #737373 50%, var(--gray-dark) 100%);
    font-family: "Questrial", sans-serif;
  }
  .back-title {
    position: absolute; left: 0; right: 0; top: 50%; transform: translateY(-50%);
    text-align: center; color: #fff; font-size: 25px; letter-spacing: 1.5px; word-spacing: 4px;
  }
  .back-rule {
    position: absolute; left: 95px; right: 95px; height: 1.5px; background: var(--orange);
  }
  .back-rule.top { top: 122px; }
  .back-rule.bottom { top: 188px; }
</style>
</head>
<body>
<main class="canvas">
  <section class="card card-front">
    <div class="photo" role="img" aria-label="Photo of two people in flight suits standing in a grassy field beside a red parachute"></div>
    <div class="identity">
      <h1 class="identity-name">Corwin T. Teller</h1>
      <p class="identity-role">Speaker, Blogger, Entrepreneur</p>
    </div>
    <ul class="contact-list">
      <li class="contact-item">
        <svg class="contact-icon" viewBox="0 0 16 16"><circle cx="8" cy="8" r="8" fill="var(--orange)"/><path d="M8 3.5a3 3 0 0 0-3 3c0 2.2 3 5.5 3 5.5s3-3.3 3-5.5a3 3 0 0 0-3-3z" fill="#fff"/><circle cx="8" cy="6.5" r="1.1" fill="var(--orange)"/></svg>
        Valtrix 320 Skyloom Airlines
      </li>
      <li class="contact-item">
        <svg class="contact-icon" viewBox="0 0 16 16"><circle cx="8" cy="8" r="8" fill="var(--orange)"/><path d="M5.4 4.2l1.5-.3.8 2-1 .8a6 6 0 0 0 2.6 2.6l.8-1 2 .8-.3 1.5c-3.6.3-6.7-2.8-6.4-6.4z" fill="#fff"/></svg>
        555.283.6094
      </li>
      <li class="contact-item">
        <svg class="contact-icon" viewBox="0 0 16 16"><circle cx="8" cy="8" r="8" fill="var(--orange)"/><g fill="none" stroke="#fff" stroke-width="1"><circle cx="8" cy="8" r="4.5"/><ellipse cx="8" cy="8" rx="2" ry="4.5"/><path d="M3.5 8h9"/></g></svg>
        www.corwinteller.com
      </li>
      <li class="contact-item">
        <svg class="contact-icon" viewBox="0 0 16 16"><circle cx="8" cy="8" r="8" fill="var(--orange)"/><rect x="4" y="5" width="8" height="6" fill="#fff"/><path d="M4 5l4 3.2L12 5" fill="none" stroke="var(--orange)" stroke-width=".9"/></svg>
        corwinteller@mailvale.net
      </li>
    </ul>
    <div class="accent-tab"></div>
  </section>

  <section class="card card-back">
    <div class="back-rule top"></div>
    <h2 class="back-title">Captain Corwin T. Teller</h2>
    <div class="back-rule bottom"></div>
  </section>
</main>
</body>
</html>
```